TIDAL VERGE needs bisness cards pronto

Bisness name is "TIDAL VERGE" new bisness the bisness includes lawn mowing, garden matanace, and any jobs around the house.
I need a card that is colorful and vibrant and the bisness of lawn mowing maybe with some nature with it. It also needs my contact details"Darren Quellby mobile 0413562049 call for free quote and email norma.vance@fernmail.com.au and a catchy tag line

Industry/Entity Type

House

Requirements
Must have
• Bisness name "TIDAL VERGE"
Contact details "0413562049"
Email norma.vance@fernmail.com.au
Call for free quote

```html
<!DOCTYPE html>
<html lang="en">
<head>
<meta charset="utf-8">
<title>Tidal Verge – Business Card</title>
<link rel="stylesheet" href="https://fonts.googleapis.com/css2?family=Archivo+Black&family=Baumans&display=swap">
<style>
  :root {
    --sky-top: #bfe6f7;
    --sky-mid: #3fa6dc;
    --sky-deep: #1f7fc2;
    --sky-glow: #eaf8ff;
    --ribbon-red: #e0192b;
    --ribbon-dark: #a80d1a;
    --ink: #111111;
    --white: #ffffff;
    --grass: #4caf2f;
    --soil: #5a3b22;
    --sign-bg: #f2f2f2;
  }
  html, body {
    margin: 0;
    padding: 0;
    width: 1200px;
    height: 777px;
    overflow: hidden;
    background: #ffffff;
  }
  .card {
    position: relative;
    width: 1200px;
    height: 777px;
    overflow: hidden;
    background:
      radial-gradient(circle at 1080px 600px, var(--sky-glow) 0, rgba(234,248,255,0.85) 90px, rgba(234,248,255,0) 330px),
      linear-gradient(180deg, var(--sky-top) 0%, #8fd0f0 28%, var(--sky-mid) 55%, var(--sky-deep) 100%);
    font-family: "Baumans", "Trebuchet MS", sans-serif;
  }
  .light-rays {
    position: absolute;
    inset: 0;
  }
  .brand-name {
    position: absolute;
    left: 28px;
    top: 10px;
    margin: 0;
    color: var(--ink);
    font-family: "Baumans", "Trebuchet MS", sans-serif;
    font-weight: 400;
    line-height: 1;
  }
  .brand-name .word-one {
    display: block;
    font-size: 132px;
  }
  .brand-name .word-two {
    display: block;
    font-size: 104px;
    margin-top: 2px;
    margin-left: 6px;
  }
  .mower-illustration {
    position: absolute;
    left: 500px;
    top: 14px;
    width: 320px;
    height: 250px;
    border-radius: 12px;
    background: linear-gradient(180deg, rgba(255,255,255,0.75), rgba(225,240,250,0.55));
  }
  .lawn-strip {
    position: absolute;
    left: 0;
    top: 258px;
    width: 1200px;
    height: 82px;
    background: linear-gradient(180deg, var(--grass) 0%, #3e8f26 38%, var(--soil) 40%, #4a2f1a 100%);
  }
  .ribbon {
    position: absolute;
    left: 0;
    top: 0;
  }
  .outlined {
    color: var(--white);
    text-shadow:
      -2px -2px 0 var(--ink), 2px -2px 0 var(--ink),
      -2px 2px 0 var(--ink), 2px 2px 0 var(--ink),
      0 -2.5px 0 var(--ink), 0 2.5px 0 var(--ink),
      -2.5px 0 0 var(--ink), 2.5px 0 0 var(--ink);
  }
  .tagline, .service, .contact-line, .email-line {
    position: absolute;
    margin: 0;
    white-space: nowrap;
    line-height: 1;
  }
  .tagline { left: 186px; top: 378px; font-size: 60px; letter-spacing: 2px; }
  .service { left: 146px; top: 484px; font-size: 56px; letter-spacing: 2px; }
  .contact-line { left: 118px; top: 586px; font-size: 58px; letter-spacing: 2px; }
  .footer-band {
    position: absolute;
    left: 0;
    top: 705px;
    width: 1200px;
    height: 72px;
    background: linear-gradient(180deg, #f04050 0%, var(--ribbon-red) 45%, var(--ribbon-dark) 100%);
  }
  .email-line { left: 26px; top: 717px; font-size: 42px; letter-spacing: 1px; }
  .owner-tab {
    position: absolute;
    right: 0;
    top: 705px;
    width: 240px;
    height: 42px;
    background: var(--sign-bg);
  }
  .owner-name {
    position: absolute;
    right: 18px;
    top: 712px;
    margin: 0;
    font-size: 20px;
    color: #333333;
    font-style: italic;
  }
</style>
</head>
<body>
<main class="card">
  <svg class="light-rays" width="1200" height="777" viewBox="0 0 1200 777" aria-hidden="true">
    <g stroke="#ffffff" stroke-opacity="0.35" stroke-width="1.5">
      <line x1="0" y1="110" x2="560" y2="110"/>
      <line x1="730" y1="350" x2="1080" y2="660"/>
      <line x1="620" y1="420" x2="840" y2="560"/>
      <line x1="0" y1="690" x2="1200" y2="690"/>
    </g>
  </svg>

  <div class="lawn-strip" role="img" aria-label="Strip of green lawn grass over brown soil"></div>
  <div class="mower-illustration" role="img" aria-label="Cartoon illustration of a gardener pushing a lawn mower across the grass"></div>

  <h1 class="brand-name">
    <span class="word-one">TIDAL</span>
    <span class="word-two">VERGE</span>
  </h1>

  <svg class="ribbon" width="1200" height="777" viewBox="0 0 1200 777" aria-hidden="false">
    <defs>
      <linearGradient id="ribbonFill" x1="0" y1="0" x2="1" y2="1">
        <stop offset="0" stop-color="#f04050"/>
        <stop offset="0.5" stop-color="#e0192b"/>
        <stop offset="1" stop-color="#a80d1a"/>
      </linearGradient>
    </defs>
    <polygon points="745,0 905,0 1200,232 1200,350" fill="url(#ribbonFill)"/>
    <text x="1012" y="160" transform="rotate(38 1012 160)" text-anchor="middle"
          font-family="Archivo Black, Arial Black, sans-serif" font-size="54"
          fill="#ffffff" stroke="#111111" stroke-width="4" paint-order="stroke">FREE QUOTE!</text>
  </svg>

  <p class="tagline outlined">Dependable &amp; Professional</p>
  <p class="service outlined">Garden maintenance</p>
  <p class="contact-line outlined">Contact: 0413562049</p>

  <div class="footer-band"></div>
  <p class="email-line outlined">Email: norma.vance@fernmail.com.au</p>
  <div class="owner-tab"></div>
  <p class="owner-name">Darren Quellby</p>
</main>
</body>
</html>
```